Wall Sticker (3 design options)

We need 3 design options for wall sticker design, taking inspiration from the Roll-Up Banner PDF files. The wall sticker will promote our school's courses and qualifications.

Size of wall sticker: 2400 mm (height) x 900 mm (width)

Wall sticker will be installed next to our classroom entrance (refer to photo of wall - file name: BRVKM Wall & Glass Panel Size.jpg

Background on our business (for your own knowledge): Our company is called Loomcraft and Apparel Skills Institute (LASKI). We help train the fashion industry as well as people who are interested in joining the fashion industry.

Must Have:
- Take colour scheme from uploaded PDF files
- Hex code for corporate colour is #DA291C (Red)
- Other Corporate Colours to be Included: Grey, White, Black

Font Type to be used: Frutiger

Logos to be used are attached: LASKI logo, PQN DLH logo, and LearnMark logo

=======================================================
This is the text content for the wall sticker:

STEP INTO THE WORLD OF FASHION

PROFESSIONAL PQN SHORT COURSES
- Fashion Styling
- Sewing and Alteration
- Leather Care
- Fabric Care

PQN ADVANCED CERTIFICATE IN FASHION TECHNOLOGY
• Apparel Design and Product Development
• Merchandising and Marketing

PQN DIPLOMA IN FASHION TECHNOLOGY:
• Footwear Design and Product Development

FUNDING & CAREER OPPORTUNITIES
Speak to us today about your eligibility in funding and potential career opportunities upon graduation.

Tel: 64829305
Email: enquiry@lasinst-mail.org
Website: www.lasinst-web.edu.sg

Stock photo: please propose stock photos for the 3 design options. The photo should 'speak' about fashion in general but not specifically on sewing, footwear making, etc but should be generic. Please do not use runway photos or photos that have fashion illustrations.

FINAL ARTWORK requirements:
- Source file format: saved for Adobe Illustrator CS6 (ai), not locked so that we can make edits in future
- Print file format: PDF (editable and not locked), must include crop marks and 3 mm bleed.

Target Market(s)

General Public, Fashionistas, Fashion Students, Aspiring Footwear Enthusiasts and people interested to enter the fashion industry

Font styles to use
Sans Serif
Other font styles liked:
• Frutiger

Colors
ec1f27
ffffff
000000
757575
c5c5c5

Requirements
Must have
• - Hex code for corporate colour is #DA291C (Red)
• - Other Corporate Colours to be Included: Grey, White, Black
• Please put in the header (at the top): LASKI logo
• Please put somewhere in the footer (bottom):
• - PQN DLH logo
• - LearnMark logo
• - our contact details and website - telephone: 64829305, email: enquiry@lasinst-mail.org, and website: www.lasinst-web.edu.sg
Should not have
• stock photo with fashion illustration

```html
<!DOCTYPE html>
<html lang="en">
<head>
<meta charset="utf-8">
<title>LASKI Wall Sticker – Step Into the World of Fashion</title>
<link rel="stylesheet" href="https://fonts.googleapis.com/css2?family=Hind:wght@400;500;700&family=Stardos+Stencil:wght@700&display=swap">
<style>
  :root {
    --brand-red: #da291c;
    --white: #ffffff;
    --black: #000000;
    --grey-dark: #757575;
    --grey-light: #c5c5c5;
    --page-bg: #f1f1f1;
    --text-dark: #1b1b1b;
    --photo-warm: #e8d6a6;
    --photo-light: #f2ece0;
  }
  * { margin: 0; padding: 0; box-sizing: border-box; }
  html, body {
    width: 900px; height: 1200px; overflow: hidden;
    background: var(--page-bg);
    font-family: "Hind", "Helvetica Neue", Arial, sans-serif;
    color: var(--text-dark);
  }
  .wall-sticker {
    position: absolute; left: 225px; top: 0;
    width: 450px; height: 1200px;
    overflow: hidden; background: var(--white);
  }
  .sticker-shapes { position: absolute; inset: 0; }
  .brand-name {
    position: absolute; right: 26px; top: 28px;
    font-size: 36px; font-weight: 400; letter-spacing: 2px;
    color: var(--black); line-height: 1;
  }
  .headline {
    position: absolute; left: 0; right: 0; top: 478px;
    text-align: center;
    font-family: "Stardos Stencil", "Hind", sans-serif;
    font-weight: 700; font-size: 50px; line-height: 58px;
    color: var(--white); letter-spacing: 1px;
  }
  .course-info {
    position: absolute; left: 34px; right: 20px; top: 702px;
  }
  .course-group { margin-bottom: 16px; }
  .course-group h2 {
    font-size: 15.5px; font-weight: 700; line-height: 20px;
    text-transform: uppercase; color: var(--text-dark);
  }
  .course-group ul { list-style: none; }
  .course-group li, .course-group p {
    font-size: 15px; line-height: 21.5px; font-weight: 400;
  }
  .course-group li::before { content: "• "; }
  .sticker-footer {
    position: absolute; left: 0; right: 0; bottom: 0; height: 64px;
    background: var(--white);
  }
  .contact-list {
    position: absolute; left: 20px; top: 14px;
    font-size: 9.5px; line-height: 13.5px;
  }
  .contact-list dt { display: inline-block; width: 42px; color: var(--grey-dark); }
  .contact-list dd { display: inline; font-weight: 700; }
  .contact-row { white-space: nowrap; }
  .partner-badge {
    position: absolute; top: 18px; height: 28px;
    background: var(--grey-light); border-radius: 4px;
  }
  .badge-dlh { left: 290px; width: 62px; }
  .badge-learnmark { left: 366px; width: 66px; }
</style>
</head>
<body>
  <main class="wall-sticker">
    <svg class="sticker-shapes" width="450" height="1200" viewBox="0 0 450 1200">
      <defs>
        <linearGradient id="photoTone" x1="0" y1="0" x2="1" y2="1">
          <stop offset="0" stop-color="#f2ece0"/>
          <stop offset="0.6" stop-color="#e8d6a6"/>
          <stop offset="1" stop-color="#d9b86a"/>
        </linearGradient>
        <linearGradient id="panelTone" x1="0" y1="0" x2="0" y2="1">
          <stop offset="0" stop-color="#eeeeee"/>
          <stop offset="1" stop-color="#d8d8d8"/>
        </linearGradient>
      </defs>
      <rect class="hero-photo" x="0" y="0" width="450" height="480" fill="url(#photoTone)" role="img" aria-label="Stock photo of hands measuring fabric with a ruler over pattern paper"/>
      <path class="red-band" d="M0,400 C140,388 300,452 450,452 L450,735 C410,700 330,664 0,662 Z" fill="var(--brand-red)"/>
      <path class="info-panel" d="M0,662 C330,664 410,700 450,735 L450,1136 L0,1136 Z" fill="url(#panelTone)"/>
    </svg>

    <div class="brand-name">LASKI</div>

    <h1 class="headline">STEP INTO<br>THE WORLD<br>OF FASHION</h1>

    <section class="course-info">
      <div class="course-group">
        <h2>Professional PQN Short Courses</h2>
        <ul>
          <li>Fashion Styling</li>
          <li>Sewing and Alteration</li>
          <li>Leather Care</li>
          <li>Fabric Care</li>
        </ul>
      </div>
      <div class="course-group">
        <h2>PQN Advanced Certificate in Fashion Technology</h2>
        <ul>
          <li>Apparel Design and Product Development</li>
          <li>Merchandising and Marketing</li>
        </ul>
      </div>
      <div class="course-group">
        <h2>PQN Diploma in Fashion Technology</h2>
        <ul>
          <li>Apparel Design and Product Development</li>
          <li>Merchandising and Marketing</li>
          <li>Footwear Design and Product Development</li>
        </ul>
      </div>
      <div class="course-group">
        <h2>Funding &amp; Career Opportunities</h2>
        <p>Speak to us today about your eligibility in funding and potential career opportunities upon graduation.</p>
      </div>
    </section>

    <footer class="sticker-footer">
      <dl class="contact-list">
        <div class="contact-row"><dt>phone</dt><dd>64829305</dd></div>
        <div class="contact-row"><dt>email</dt><dd>enquiry@lasinst-mail.org</dd></div>
        <div class="contact-row"><dt>website</dt><dd>www.lasinst-web.edu.sg</dd></div>
      </dl>
      <div class="partner-badge badge-dlh" role="img" aria-label="PQN DLH partner badge"></div>
      <div class="partner-badge badge-learnmark" role="img" aria-label="LearnMark certification badge"></div>
    </footer>
  </main>
</body>
</html>
```